Banner publicitario para certamen de frases "CitasDelViento.net"

Con motivo del lanzamiento de nuestra página web [login to view URL] vamos a convocar un Certamen de frases online. Para ello necesitamos un banner publicitario que incluya el siguiente contenido:
¡GANA 100 EUROS POR UNA FRASE!
I CERTAMEN DE FRASES "[login to view URL]"
y un boton a la acción que diga "PARTICIPA AQUI", por ejemplo.

Las medidas que necesitamos son las tipicas para twitter, instagram, facebook, y despues para ad Sense y uno horizontal para nuestra web.

Deberá entregarse el fichero fuente en photoshop o en el software desarrollado para futuras modificaciones.
Saludos

```html
<!DOCTYPE html>
<html lang="es">
<head>
<meta charset="utf-8">
<title>I Certamen de Frases – CitasDelViento.net</title>
<link href="https://fonts.googleapis.com/css2?family=Antonio:wght@100;200;300;400&family=Oswald:wght@300;400&display=swap" rel="stylesheet">
<style>
  :root {
    --backdrop: #a9d4da;
    --white: #ffffff;
    --coral: #f5434b;
    --slate: #4e5478;
    --orange: #ef6a3c;
    --ink: #151515;
    --navy-ink: #3f4670;
    --cream: #f7efe2;
    --sky-top: #5d6590;
    --sky-mid: #c9768f;
    --sunset: #f56a3e;
    --sea: #8d8ea6;
  }
  * { margin: 0; padding: 0; box-sizing: border-box; }
  html, body { width: 867px; height: 1200px; overflow: hidden; }
  body { background: var(--backdrop); position: relative; font-family: "Antonio", "Oswald", sans-serif; }

  .sunset-photo { position: absolute; }
  .poster-backdrop, .banner-backdrop { inset: 0; }
  .poster-backdrop {
    background: linear-gradient(180deg, var(--sky-top) 0%, var(--sky-mid) 28%, #e8556b 45%, var(--sunset) 58%, #f59a5a 63%, #d86a6a 72%, var(--sea) 100%);
  }

  /* Vertical poster */
  .poster { position: absolute; left: 144px; top: 55px; width: 600px; height: 841px; box-shadow: 2px 3px 6px rgba(0,0,0,.35); }
  .poster-frame { position: absolute; left: 43px; top: 45px; width: 518px; height: 757px; background: var(--white); }
  .tagline { position: absolute; left: 0; right: 0; top: 13px; text-align: center; font-family: "Oswald", sans-serif; font-style: italic; font-size: 11.5px; color: var(--ink); letter-spacing: .2px; }
  .poster-photo { left: 38px; top: 43px; width: 437px; height: 411px;
    background: linear-gradient(180deg, #6a6d96 0%, #c66d8c 25%, #f0596a 45%, #f47a4a 65%, #ffb05a 82%, #e55a55 92%, #9a6e80 100%); }
  .headline-box { position: absolute; left: 66px; top: 80px; width: 378px; height: 299px; background: var(--coral); display: flex; align-items: center; justify-content: center; }
  .headline { color: var(--white); font-weight: 300; font-size: 57px; line-height: 1.24; text-align: center; letter-spacing: 1px; }
  .year-tag { position: absolute; left: 179px; top: 431px; width: 157px; height: 53px; background: var(--slate); color: var(--white); font-size: 44px; font-weight: 300; display: flex; align-items: center; justify-content: center; letter-spacing: 1px; }
  .contest-title { position: absolute; left: 0; right: 0; top: 506px; text-align: center; font-weight: 100; font-size: 54px; color: var(--ink); letter-spacing: 3px; transform: skewX(-8deg); }
  .contest-site { position: absolute; left: 0; right: 0; top: 594px; text-align: center; font-weight: 400; font-size: 42px; color: var(--ink); letter-spacing: 1px; transform: skewX(-10deg); }
  .cta { position: absolute; background: var(--orange); color: var(--cream); display: flex; align-items: center; justify-content: center; font-weight: 400; letter-spacing: 1px; text-shadow: 1px 1px 1px rgba(0,0,0,.4); }
  .poster .cta { left: 154px; top: 760px; width: 298px; height: 78px; font-size: 34px; }

  /* Horizontal banner */
  .banner { position: absolute; left: 87px; top: 946px; width: 714px; height: 183px; box-shadow: 2px 3px 6px rgba(0,0,0,.35); }
  .banner-backdrop { background: linear-gradient(90deg, #e0707f 0%, #c9768f 25%, #8a7fa0 50%, #6d6f93 75%, #b27a94 100%); }
  .banner-headline { position: absolute; left: 19px; top: 20px; width: 215px; height: 144px; background: var(--coral); color: var(--white); font-weight: 300; font-size: 35px; line-height: 1.2; text-align: center; display: flex; align-items: center; justify-content: center; letter-spacing: 1px; }
  .banner-panel { position: absolute; left: 258px; top: 20px; width: 432px; height: 142px; background: var(--white); text-align: center; color: var(--navy-ink); }
  .banner-title { margin-top: 12px; font-weight: 200; font-size: 38px; letter-spacing: 2px; transform: skewX(-10deg); }
  .banner-site { font-weight: 300; font-size: 31px; letter-spacing: 1px; transform: skewX(-10deg); line-height: 1.1; }
  .banner .cta { left: 375px; top: 139px; width: 191px; height: 42px; font-size: 22px; }
</style>
</head>
<body>
  <section class="poster">
    <div class="sunset-photo poster-backdrop" role="img" aria-label="Fotografía de un atardecer sobre el mar con nubes rosadas"></div>
    <div class="poster-frame">
      <p class="tagline">Las frases más bonitas del mundo recopiladas en un único sitio web.</p>
      <div class="sunset-photo poster-photo" role="img" aria-label="Fotografía de un atardecer naranja sobre el horizonte marino"></div>
      <div class="headline-box"><h1 class="headline">¡GANA 100 EUROS<br>POR UNA FRASE!</h1></div>
      <div class="year-tag">2020</div>
      <h2 class="contest-title">I CERTAMEN DE FRASES</h2>
      <p class="contest-site">"CITASDELVIENTO.NET"</p>
    </div>
    <div class="cta">PARTICIPA AQUI</div>
  </section>

  <section class="banner">
    <div class="sunset-photo banner-backdrop" role="img" aria-label="Fotografía de un cielo al atardecer con nubes rosas y violetas"></div>
    <div class="banner-headline">¡GANA 100<br>EUROS POR<br>UNA FRASE!</div>
    <div class="banner-panel">
      <p class="banner-title">I CERTAMEN DE FRASES</p>
      <p class="banner-site">"CITASDELVIENTO.NET"</p>
    </div>
    <div class="cta">PARTICIPA AQUI</div>
  </section>
</body>
</html>
```